Disease outbreak warning

I need a flyer that explains to hunters how to act as frontline responders to potential disease outbreaks in wildlife populations. In this case the disease is African Swine Fever. We need an at a glance style with plenty of colour and that’s very easy to read.

I HAVE ATTACHED SOME EXISTING FLYERS FROM OVERSEAS ETC THAT CONTAIN SOME OF THE RELEVANT INFO. THEY ARE TO BE USED AS A GUIDE ONLY.
Updates

Need to see some more options. We have some that can be developed successfully but we’d like to see some more options that will suit a national campaign.

Target Market(s)

Australian hunters encountering wild pigs. Typical age is from 18 to 32 but can be older. Male or female.

Colors

Designer to choose colors to be used in the design.

Requirements
Must have
• The KVRTE logo (supplied). It should be relatively small at the bottom of the page. Plus we need room for two or three other logos that can be overprinted on the project if required.
• Must have information for hunters as the main focus.
Nice to have
• A double sided flyer.
Should not have
• US spelling.

```html
<!DOCTYPE html>
<html lang="en-AU">
<head>
<meta charset="utf-8">
<title>African Swine Fever – Hunter Flyer</title>
<link href="https://fonts.googleapis.com/css2?family=Libre+Baskerville:wght@700&family=Open+Sans:wght@400;600;700;800&display=swap" rel="stylesheet">
<style>
  :root{
    --navy:#1a2260;
    --navy-deep:#121845;
    --navy-mid:#27328a;
    --white:#ffffff;
    --ink:#1d1d2b;
    --stage:#3a3a3c;
    --orange:#f39a1e;
    --olive:#5d5a2c;
    --grass:#5d7a3a;
  }
  *{box-sizing:border-box;margin:0;padding:0}
  html,body{width:1200px;height:800px;overflow:hidden}
  body{background:var(--stage);font-family:"Open Sans",Arial,sans-serif;position:relative}

  .flyer{position:absolute;top:30px;width:560px;height:740px;background:var(--navy);overflow:hidden;color:var(--white)}
  .flyer--front{left:30px}
  .flyer--back{left:610px}

  /* Front */
  .masthead{height:150px;position:relative;display:flex;justify-content:space-between;padding:14px 0 0 22px}
  .masthead__art{position:absolute;left:150px;top:8px;width:190px;height:138px;border-radius:50%;background:radial-gradient(ellipse at center,rgba(120,70,90,.55),rgba(60,70,120,.25) 60%,transparent 75%)}
  .masthead__title{position:relative;font-family:"Libre Baskerville",Georgia,serif;font-weight:700;font-size:40px;line-height:38px;color:var(--white)}
  .masthead__brand{width:208px;height:110px;background:var(--white);margin:6px 0 0;display:flex;align-items:center;justify-content:center;gap:10px}
  .brand-dot{width:22px;height:22px;border-radius:50%;background:var(--orange)}
  .brand-name{font-weight:800;font-size:26px;color:var(--navy);letter-spacing:1px}

  .intro{background:var(--white);color:var(--ink);font-size:11px;line-height:13.5px;padding:12px 20px 10px;height:80px}
  .banner{height:40px;display:flex;align-items:center;justify-content:center;font-weight:700;font-size:22px;border-bottom:2px solid var(--white)}

  .columns{display:flex;height:470px}
  .col-signs{width:230px;border-right:3px solid var(--white)}
  .panel{padding:10px 12px 0 20px}
  .panel--signs{height:268px;border-bottom:2px solid var(--white)}
  .panel--carcass{padding-left:15px}
  .panel__head{font-size:17px;line-height:22px;text-transform:uppercase;font-weight:400;margin-bottom:6px}
  .panel__head strong{font-weight:700}
  .panel ol{list-style:none;font-size:11px;line-height:16.5px;text-transform:uppercase}

  .col-action{flex:1;display:flex;flex-direction:column}
  .photo{height:272px;background:linear-gradient(180deg,#6c8fb3 0%,#8aa06a 30%,var(--grass) 55%,#3b3028 75%,#4a3d30 100%)}
  .action-band{height:48px;display:flex;align-items:center;justify-content:center;font-weight:700;font-size:23px;letter-spacing:.5px}
  .action-body{flex:1;background:var(--white);color:var(--ink);text-align:center;padding:16px 18px 0}
  .action-body p{font-size:13.5px;line-height:21px;text-transform:uppercase}
  .action-body p strong{font-weight:700}
  .hotline{margin-top:10px;height:38px;background:var(--navy);color:var(--white);display:flex;align-items:center;justify-content:center;gap:12px;font-weight:700;font-size:21px}

  /* Back */
  .back-head{background:var(--white);height:72px;display:flex;align-items:center;padding-left:26px;color:var(--navy);font-weight:800;font-size:24px}
  .steps{height:196px;padding:14px 26px 0;background:linear-gradient(180deg,var(--navy-deep),var(--navy-mid))}
  .steps ol,.donts ol{list-style:none;text-transform:uppercase;font-size:12px;line-height:23px}
  .donts{background:var(--white);color:var(--navy);height:190px;padding:12px 26px 0}
  .donts h2{font-weight:800;font-size:20px;margin-bottom:2px}
  .donts ol{line-height:21px}
  .feature{position:relative;height:282px;background:linear-gradient(160deg,var(--olive) 0%,var(--orange) 45%,var(--orange) 60%,var(--navy) 100%);display:flex;justify-content:center;padding-top:22px}
  .feature__name{font-weight:800;font-size:64px;color:var(--white);letter-spacing:4px}
  .cta-box{position:absolute;left:60px;right:60px;top:130px;height:94px;background:var(--navy);border:2px solid var(--white);text-align:center;padding-top:10px}
  .cta-box p{font-size:12px;line-height:17px;text-transform:uppercase}
  .cta-box strong{font-weight:700}
  .cta-box .hotline{margin-top:4px;height:30px;font-size:20px;background:none}
  .footer-note{position:absolute;left:0;right:0;bottom:10px;text-align:center;font-size:9px;line-height:12px;text-transform:uppercase}
</style>
</head>
<body>

<article class="flyer flyer--front">
  <header class="masthead">
    <div class="masthead__art" role="img" aria-label="Faint map of Australia with two pig heads"></div>
    <h1 class="masthead__title">African<br>Swine<br>Fever</h1>
    <div class="masthead__brand">
      <span class="brand-dot"></span><span class="brand-name">KVRTE</span>
    </div>
  </header>

  <p class="intro">Sub heading: Hunters are on the Australian Biosecurity frontline Intro copy: African Swine Fever is on our doorstep and hunters should be on the lookout for any sign ASF has reached our shores. It has the potential to destroy Australia’s domestic pork industry and cause widespread hunting bans. It must be contained.</p>

  <div class="banner">Early detection is vital</div>

  <div class="columns">
    <div class="col-signs">
      <section class="panel panel--signs">
        <h2 class="panel__head">The signs of<br><strong>African Swine Fever</strong><br>in pigs can include:</h2>
        <ol>
          <li>1. Death (possibly before other signs are noticeable)</li>
          <li>2. Blotching/reddening of the skin</li>
          <li>3. High fever</li>
          <li>4. Lack of coordination or stiff gait</li>
          <li>5. Difficulty breathing</li>
          <li>6. Abortion</li>
          <li>7. Diarrhoea</li>
          <li>8. Vomiting</li>
        </ol>
      </section>
      <section class="panel panel--carcass">
        <h2 class="panel__head">Inspect <strong>carcasses</strong><br>for:</h2>
        <ol>
          <li>1. Pinpoint reddening in organs such as heart and kidneys</li>
          <li>2. Reddening of the skin</li>
          <li>3. Excess fluid around the heart</li>
          <li>4. Enlarged lymph nodes resembling blood clots</li>
          <li>5. Enlarged, fragile and/or dark-coloured spleen</li>
        </ol>
      </section>
    </div>

    <div class="col-action">
      <div class="photo" role="img" aria-label="Photograph of a feral boar lying on grass beside a log"></div>
      <div class="action-band">CALL TO ACTION</div>
      <div class="action-body">
        <p>If you suspect ASF, call<br><strong>The Emergency Animal Disease Hotline</strong></p>
        <div class="hotline">
          <svg width="30" height="24" viewBox="0 0 30 24" aria-hidden="true"><path d="M2 8c0-4 6-6 13-6s13 2 13 6v2h-6V7c-2-1-5-1-7-1s-5 0-7 1v3H2z" fill="#fff"/><path d="M7 10h16l3 12H4z" fill="#fff"/><g fill="#1a2260"><circle cx="11" cy="14" r="1.2"/><circle cx="15" cy="14" r="1.2"/><circle cx="19" cy="14" r="1.2"/><circle cx="11" cy="18" r="1.2"/><circle cx="15" cy="18" r="1.2"/><circle cx="19" cy="18" r="1.2"/></g></svg>
          1800 555 010
        </div>
      </div>
    </div>
  </div>
</article>

<article class="flyer flyer--back">
  <h2 class="back-head">TO PREVENT THE SPREAD OF DISEASE</h2>
  <section class="steps">
    <ol>
      <li>1. Wear disposable or washable protective clothing<br>(aprons / gloves / overalls) when dressing feral pigs</li>
      <li>2. Inspect all carcasses and carcass parts for evidence of disease or illness</li>
      <li>3. Clean and disinfect all equipment on site</li>
      <li>4. Respect all quarantines, biosecurity plans and restrictions in place</li>
      <li>5. Only hunt on one property each hunt</li>
      <li>6. Thoroughly clean and disinfect vehicle after each hunt</li>
    </ol>
  </section>
  <section class="donts">
    <h2>DO NOT</h2>
    <ol>
      <li>1. Have contact with domestic pigs if you hunt feral pigs</li>
      <li>2. Move live animals (including piglets) to new locations</li>
      <li>3. Keep feral pigs at home</li>
      <li>4. Use swill (meat and food scraps) to feed or trap feral pigs</li>
      <li>5. Leave leftovers from your meals in the hunting area</li>
      <li>6. Feed raw feral pork to dogs</li>
    </ol>
  </section>
  <section class="feature">
    <span class="feature__name">KVRTE</span>
    <div class="cta-box">
      <p>Call to action: if you suspect ASF, call<br><strong>The Emergency Animal Disease Hotline</strong></p>
      <div class="hotline">
        <svg width="28" height="22" viewBox="0 0 30 24" aria-hidden="true"><path d="M2 8c0-4 6-6 13-6s13 2 13 6v2h-6V7c-2-1-5-1-7-1s-5 0-7 1v3H2z" fill="#fff"/><path d="M7 10h16l3 12H4z" fill="#fff"/><g fill="#1a2260"><circle cx="11" cy="14" r="1.2"/><circle cx="15" cy="14" r="1.2"/><circle cx="19" cy="14" r="1.2"/><circle cx="11" cy="18" r="1.2"/><circle cx="15" cy="18" r="1.2"/><circle cx="19" cy="18" r="1.2"/></g></svg>
        1800 555 010
      </div>
    </div>
    <p class="footer-note">The KVRTE Hunters Association,<br>a part of Australia’s biosecurity network PH 1300 555 247</p>
  </section>
</article>

</body>
</html>
```